TideLantern business card design

I would like a design that shows people that TideLantern is about using SOUND as a tool in ALL areas and stages of life - during labour, during motherhood, when a baby, child, adult at work, while sick, when dying, when celebrating.... there are MANY different pathways that the power of sound can be incorporated to help people relax, energise and connect with themselves and others.
The logo is purple...I can see pathways, swirling, colours, musical notes or sound waves.... white background on front. Can have different colour on back...I'm flexible and open to suggestions.

Target Market(s)

at the moment it is mostly expectant couples and mothers... but it really is for anyone who is looking for an alternative to "traditional" medicine

Industry/Entity Type

Adult

Contact Information for Business Card

Harriet Quenby - founder
0437162894
www.tidelantern.com.au
harriet@tidelantern.com.au
tidecradle
tidefrolic
tidenourishing
tidegatherings
tidekneading

Colors

Designer to choose colors to be used in the design.

Requirements
Must have
• logo
music notes/soundwaves - something that represents sound affecting people
something that represents pathways and/or connection

```html
<!DOCTYPE html>
<html lang="en">
<head>
<meta charset="utf-8">
<title>TideLantern business cards</title>
<link rel="stylesheet" href="https://fonts.googleapis.com/css2?family=Jost:wght@400;500;700&display=swap">
<style>
  :root {
    --purple: #922a8e;
    --purple-deep: #7d1f7a;
    --ink: #4a4a4a;
    --card: #ffffff;
    --backdrop: #e4e3e6;
    --hairline: #ececee;
  }
  * { box-sizing: border-box; margin: 0; padding: 0; }
  html, body {
    width: 1200px; height: 900px; overflow: hidden;
    background: var(--backdrop);
    font-family: "Jost", "Futura", sans-serif;
  }
  .sheet {
    position: relative; width: 1200px; height: 900px;
    display: flex; flex-direction: column; align-items: center; justify-content: center; gap: 40px;
  }
  .card {
    position: relative; width: 640px; height: 390px;
    background: var(--card);
    border: 11px solid var(--purple);
    box-shadow: 0 10px 24px rgba(0,0,0,0.12);
    overflow: hidden;
  }

  /* Front */
  .front__tab {
    position: absolute; background: var(--purple); height: 44px; width: 150px;
  }
  .front__tab--top { top: 0; left: 215px; }
  .front__tab--bottom { bottom: 0; left: 330px; }
  .front__rule {
    position: absolute; left: 40px; right: 40px; height: 1px; background: var(--hairline);
  }
  .front__rule--top { top: 44px; }
  .front__rule--bottom { bottom: 44px; }
  .brand {
    position: absolute; inset: 0;
    display: flex; flex-direction: column; align-items: center; justify-content: center;
  }
  .brand__lockup { display: flex; align-items: center; gap: 14px; }
  .brand__dot {
    width: 34px; height: 34px; border-radius: 50%; background: var(--purple);
  }
  .brand__name {
    font-size: 50px; font-weight: 400; color: var(--purple); letter-spacing: -0.5px; line-height: 1;
  }
  .brand__tagline {
    margin-top: 10px; font-size: 17px; font-weight: 400; color: var(--ink); letter-spacing: 0.3px;
  }

  /* Back */
  .services {
    position: absolute; top: 0; left: 250px; width: 170px; height: 176px;
    background: var(--purple); border-radius: 0 0 12px 12px;
    display: flex; flex-direction: column; align-items: center; justify-content: center;
    list-style: none; color: #fff; font-size: 19px; line-height: 1.12; letter-spacing: 0.3px;
  }
  .contact {
    position: absolute; left: 0; right: 0; top: 190px; text-align: center; padding-left: 140px;
    color: var(--purple);
  }
  .contact__name {
    font-size: 30px; font-weight: 700; letter-spacing: 0.5px; line-height: 1;
  }
  .contact__role {
    font-size: 25px; font-weight: 400; color: var(--purple-deep); line-height: 1.05;
  }
  .contact__phone {
    margin-top: 10px; font-size: 19px; letter-spacing: 1px; line-height: 1.2;
  }
  .contact__lines {
    position: absolute; right: 22px; top: 278px; font-size: 18px; line-height: 1.2;
    color: var(--purple); letter-spacing: 0.3px; white-space: nowrap;
  }
  .contact__web {
    position: absolute; left: 22px; bottom: 12px; font-size: 26px; line-height: 1.2;
    color: var(--purple); letter-spacing: 0.5px; white-space: nowrap;
  }
</style>
</head>
<body>
<main class="sheet">
  <section class="card card--front" aria-label="Card front">
    <div class="front__tab front__tab--top"></div>
    <div class="front__rule front__rule--top"></div>
    <div class="brand">
      <div class="brand__lockup">
        <span class="brand__dot"></span>
        <span class="brand__name">TideLantern</span>
      </div>
      <p class="brand__tagline">listening along every path</p>
    </div>
    <div class="front__rule front__rule--bottom"></div>
    <div class="front__tab front__tab--bottom"></div>
  </section>

  <section class="card card--back" aria-label="Card back">
    <ul class="services">
      <li>tidegatherings</li>
      <li>tidekneading</li>
      <li>tidenourishing</li>
      <li>tidecradle</li>
      <li>tidefrolic</li>
    </ul>
    <div class="contact">
      <p class="contact__name">HARRIET QUENBY</p>
      <p class="contact__role">FOUNDER</p>
      <p class="contact__phone">0437162894</p>
    </div>
    <p class="contact__lines">tidelantern.com.au | harriet@tidelantern.com.au</p>
    <p class="contact__web">www.tidelantern.com.au</p>
  </section>
</main>
</body>
</html>
```